"Brelunda" sparkling beverage

Dear All!
I need a stick label (82*95 - front label, 82*65 - back label )design for а sparkling beverage, name is "Brelunda", 4 flavours: lemonade,duchess pear, estragon, original. Transparent glass bottles 0,5 liter (alumnium closure 28*15)/0,33 liter (crown cap), neck label should also be on the bottle 0,5 liter.
European style is welcomed
Do not send the disigns with a little changes several times, please!!!
Target Market(s)
Young people from 12-30 ages old
Look and feel
Each slider illustrates characteristics of the customer's brand and the style your logo design should communicate.

```html
<!DOCTYPE html>
<html lang="en">
<head>
<meta charset="utf-8">
<title>Brelunda – Sparkling Beverage Labels</title>
<link href="https://fonts.googleapis.com/css2?family=Fredoka:wght@600&display=swap" rel="stylesheet">
<style>
  :root {
    --bg: #ffffff;
    --brand-green: #7cc520;
    --ink-green: #4f7d1c;
    --pear-gold: #c9a21c;
    --pear-band: #d2b400;
    --pear-fill-bottom: #d6bd00;
    --lemon-band: #f5e000;
    --lemon-gold: #f2cf12;
    --lemon-fill-bottom: #f7e41e;
    --art-pear-light: #f4ea6a;
    --art-pear-mid: #d9cb2a;
    --art-pear-deep: #a99d1a;
    --art-lemon-light: #fff39a;
    --art-lemon-mid: #fbe03a;
    --art-lemon-deep: #f2bf0a;
  }
  * { margin: 0; padding: 0; box-sizing: border-box; }
  html, body { width: 1200px; height: 846px; overflow: hidden; background: var(--bg); }
  body { position: relative; font-family: "Fredoka", "Arial Rounded MT Bold", sans-serif; font-weight: 600; }

  .wordmark {
    position: absolute; left: 136px; top: 112px; width: 400px;
    text-align: center; font-size: 100px; line-height: 1; color: var(--brand-green);
  }

  .label {
    position: absolute; width: 307px; height: 355px;
    background: #fff; overflow: hidden;
    box-shadow: 0 1px 3px rgba(0,0,0,.18);
  }
  .label--pear { left: 30px; top: 377px; }
  .label--lemon { left: 361px; top: 377px; }
  .label--small { transform: scale(0.58); transform-origin: 0 0; }
  .label--small.label--pear { left: 750px; top: 449px; }
  .label--small.label--lemon { left: 958px; top: 449px; }

  .label__band { position: absolute; left: 0; top: 0; width: 100%; height: 10px; }
  .label--pear .label__band { background: var(--pear-band); }
  .label--lemon .label__band { background: var(--lemon-band); }

  .label__fizz { position: absolute; left: 0; bottom: 0; width: 100%; height: 160px; }
  .label--pear .label__fizz { background: linear-gradient(to bottom, rgba(255,255,255,0), var(--pear-fill-bottom)); }
  .label--lemon .label__fizz { background: linear-gradient(to bottom, rgba(255,255,255,0), var(--lemon-fill-bottom)); }

  .label__art { position: absolute; }
  .label--pear .label__art {
    left: 14px; top: 16px; width: 240px; height: 178px;
    border-radius: 38% 62% 44% 56% / 52% 48% 52% 48%;
    background: radial-gradient(ellipse at 68% 62%, var(--art-pear-deep) 0%, var(--art-pear-mid) 38%, var(--art-pear-light) 72%, rgba(244,234,106,0) 100%);
  }
  .label--lemon .label__art {
    left: 36px; top: 22px; width: 236px; height: 172px;
    border-radius: 46% 54% 40% 60% / 56% 50% 50% 44%;
    background: radial-gradient(ellipse at 45% 64%, var(--art-lemon-deep) 0%, var(--art-lemon-mid) 42%, var(--art-lemon-light) 74%, rgba(255,243,154,0) 100%);
  }

  .label__flavour {
    position: absolute; right: 10px; top: 48px;
    font-size: 21px; line-height: 1.1; text-align: center;
    color: var(--pear-gold); transform: rotate(8deg);
  }
  .label__flavour-arc { position: absolute; right: 0; top: 12px; width: 180px; height: 110px; }

  .label__dot { position: absolute; border-radius: 50%; background: var(--lemon-gold); }
  .label__dot--big { left: 16px; top: 30px; width: 26px; height: 26px; }
  .label__dot--small { left: 16px; top: 118px; width: 18px; height: 18px; }

  .label__name {
    position: absolute; left: 0; top: 192px; width: 100%;
    text-align: center; font-size: 66px; line-height: 1; color: var(--brand-green);
  }

  .label__tagline {
    position: absolute; left: 20px; bottom: 34px;
    font-size: 20px; line-height: 1; color: var(--ink-green);
    transform: rotate(-6deg); text-transform: uppercase;
  }
  .label__tagline span { display: block; padding-left: 8px; }
</style>
</head>
<body>

  <div class="wordmark">Brelunda</div>

  <section class="label label--pear">
    <div class="label__band"></div>
    <div class="label__fizz" role="img" aria-label="Rising bubbles over a golden gradient"></div>
    <div class="label__art" role="img" aria-label="Illustration of a whole and halved duchess pear in a juice splash"></div>
    <div class="label__flavour">DUCHESS<br>PEAR</div>
    <div class="label__name">Brelunda</div>
    <div class="label__tagline">Sparkling<span>Beverage</span></div>
  </section>

  <section class="label label--lemon">
    <div class="label__band"></div>
    <div class="label__fizz" role="img" aria-label="Rising bubbles over a lemon yellow gradient"></div>
    <div class="label__art" role="img" aria-label="Illustration of a lemon and lemon slice in a juice splash"></div>
    <div class="label__dot label__dot--big"></div>
    <div class="label__dot label__dot--small"></div>
    <svg class="label__flavour-arc" viewBox="0 0 180 110" aria-label="Lemonade">
      <defs><path id="lemon-arc-a" d="M20,40 Q120,25 170,110"/></defs>
      <text font-family="Fredoka, sans-serif" font-weight="600" font-size="21" fill="#f2cf12" letter-spacing="2">
        <textPath href="#lemon-arc-a">LEMONADE</textPath>
      </text>
    </svg>
    <div class="label__name">Brelunda</div>
    <div class="label__tagline">Sparkling<span>Beverage</span></div>
  </section>

  <section class="label label--pear label--small">
    <div class="label__band"></div>
    <div class="label__fizz" role="img" aria-label="Rising bubbles over a golden gradient"></div>
    <div class="label__art" role="img" aria-label="Illustration of a whole and halved duchess pear in a juice splash"></div>
    <div class="label__flavour">DUCHESS<br>PEAR</div>
    <div class="label__name">Brelunda</div>
    <div class="label__tagline">Sparkling<span>Beverage</span></div>
  </section>

  <section class="label label--lemon label--small">
    <div class="label__band"></div>
    <div class="label__fizz" role="img" aria-label="Rising bubbles over a lemon yellow gradient"></div>
    <div class="label__art" role="img" aria-label="Illustration of a lemon and lemon slice in a juice splash"></div>
    <div class="label__dot label__dot--big"></div>
    <div class="label__dot label__dot--small"></div>
    <svg class="label__flavour-arc" viewBox="0 0 180 110" aria-label="Lemonade">
      <defs><path id="lemon-arc-b" d="M20,40 Q120,25 170,110"/></defs>
      <text font-family="Fredoka, sans-serif" font-weight="600" font-size="21" fill="#f2cf12" letter-spacing="2">
        <textPath href="#lemon-arc-b">LEMONADE</textPath>
      </text>
    </svg>
    <div class="label__name">Brelunda</div>
    <div class="label__tagline">Sparkling<span>Beverage</span></div>
  </section>

</body>
</html>
```